DAF - EXPO

We are a sport event orgnizer managing diffrent sport events. We would like to orgnize the kick off event of the season Dunlore Athletic Fairs expo will be the gathering point of all sports events happening in Kuwait.
The expected events like Marathons, Forgelift , Triathlons , Karting , Inline skates , BMX.

Target Market(s)
Target market are outdoor and sports enthusiast
Industry/Entity Type
Events
Requirements
Must have
- Name of the event Dunlore Athletic Fairs EXPO
Dates 4-5 October 2013
Location Harbel Quayfront
Snapwell account and Chirplane Zelvoracedays
website www.tarn-wicklo.com.kw
Logos of the events who will participate attached
Nice to have
- Facts:
10 Events
8 Sports
6 Locations
5000+ Participants
in 5 Months ( in big bold so it can be the highlight )

```html
<!DOCTYPE html>
<html lang="en">
<head>
<meta charset="utf-8">
<title>Dunlore Athletic Fairs EXPO</title>
<link href="https://fonts.googleapis.com/css2?family=Archivo+Black&family=Arimo:ital,wght@0,700;1,700&display=swap" rel="stylesheet">
<style>
  :root {
    --orange: #f26a1b;
    --orange-deep: #d9530e;
    --ink: #111111;
    --panel: #161616;
    --paper: #ffffff;
    --muted: #cfcfcf;
    --backdrop: #2b2b2b;
    --runners-a: #6e6a66;
    --runners-b: #3e3b39;
    --weights-a: #b33a22;
    --weights-b: #4a4a4a;
  }
  * { box-sizing: border-box; margin: 0; padding: 0; }
  html, body { width: 1200px; height: 910px; overflow: hidden; }
  body {
    background: var(--backdrop);
    font-family: "Arimo", Arial, sans-serif;
    position: relative;
  }
  .flyer {
    position: absolute;
    left: 290px; top: 25px;
    width: 620px; height: 860px;
    background: var(--panel);
    overflow: hidden;
  }
  .layer { position: absolute; left: 0; top: 0; width: 620px; height: 860px; }
  .photo-runners {
    height: 470px;
    background: linear-gradient(160deg, var(--runners-a) 0%, #8a8580 40%, var(--runners-b) 100%);
  }
  .header-band {
    background: linear-gradient(90deg, var(--orange-deep), var(--orange));
    clip-path: polygon(0 22px, 620px 0, 620px 92px, 330px 116px, 0 104px);
  }
  .event-title {
    position: absolute; left: 20px; top: 36px;
    font-family: "Archivo Black", "Arial Black", sans-serif;
    font-weight: 400;
    font-size: 35px; color: var(--paper);
    transform: rotate(-2deg) skewX(-10deg);
    transform-origin: left center;
    white-space: nowrap;
  }
  .info-band {
    background: var(--paper);
    clip-path: polygon(0 380px, 620px 372px, 620px 505px, 0 470px);
  }
  .info-accent {
    background: var(--orange);
    clip-path: polygon(330px 488px, 620px 505px, 620px 514px, 330px 494px);
  }
  .weights-frame {
    background: var(--orange);
    clip-path: polygon(250px 250px, 620px 140px, 620px 470px);
  }
  .photo-weights {
    background: linear-gradient(135deg, var(--weights-a) 0%, #7a3a2a 45%, var(--weights-b) 100%);
    clip-path: polygon(280px 252px, 620px 152px, 620px 450px);
  }
  .event-details {
    position: absolute; left: 36px; top: 396px;
    font-weight: 700; font-size: 30px; line-height: 38px;
    color: var(--ink);
    transform: rotate(-1deg);
  }
  .event-details .value { color: var(--orange); }
  .facts {
    position: absolute; left: 26px; top: 530px;
    font-family: "Archivo Black", "Arial Black", sans-serif;
    font-weight: 400;
    font-size: 23px; line-height: 30px;
    color: var(--orange);
    transform: skewX(-8deg);
    transform-origin: left top;
    white-space: nowrap;
  }
  .facts .facts-label { color: var(--paper); }
  .social {
    position: absolute; right: 32px; top: 548px;
    text-align: right;
    font-style: italic; font-weight: 700;
    font-size: 18px; line-height: 22px;
    color: var(--paper);
  }
  .social-links {
    position: absolute; right: 32px; top: 604px;
    display: flex; gap: 26px;
  }
  .social-item {
    display: flex; align-items: center; gap: 8px;
    font-weight: 700; font-size: 16px; color: var(--paper);
  }
  .social-item .mark { width: 18px; height: 18px; background: var(--orange); }
  .website {
    position: absolute; right: 32px; top: 650px;
    font-weight: 700; font-size: 17px;
    color: var(--orange);
  }
  .partner-strip {
    position: absolute; left: 0; top: 740px;
    width: 620px; height: 120px;
    background: var(--paper);
    display: flex; flex-wrap: wrap;
    justify-content: space-around; align-content: center;
    row-gap: 18px; column-gap: 20px;
    padding: 10px 20px;
  }
  .partner {
    display: flex; align-items: center; gap: 8px;
    font-weight: 700; font-size: 19px; color: var(--ink);
  }
  .partner .dot { width: 16px; height: 16px; border-radius: 50%; background: var(--orange); }
  .partner .square { width: 16px; height: 16px; background: var(--orange); }
</style>
</head>
<body>
  <main class="flyer">
    <div class="layer photo-runners" role="img" aria-label="Photo of marathon runners' legs on a sunny road"></div>
    <div class="layer info-band"></div>
    <div class="layer info-accent"></div>
    <div class="layer weights-frame"></div>
    <div class="layer photo-weights" role="img" aria-label="Photo of a rack of red dumbbells in a gym"></div>
    <div class="layer header-band"></div>
    <h1 class="event-title">Dunlore Athletic Fairs EXPO</h1>

    <p class="event-details">
      Dates <span class="value">4-5 October 2013</span><br>
      Location <span class="value">Harbel Quayfront</span>
    </p>

    <p class="facts">
      <span class="facts-label">Facts:</span><br>
      10 Events<br>
      8 Sports<br>
      6 Locations<br>
      5000+ Participants<br>
      in 5 Months
    </p>

    <p class="social">Snapwell account<br>and Chirplane Zelvoracedays</p>
    <div class="social-links">
      <span class="social-item"><span class="mark"></span>Snapwell</span>
      <span class="social-item"><span class="mark"></span>Chirplane</span>
    </div>
    <p class="website">www.tarn-wicklo.com.kw</p>

    <section class="partner-strip">
      <span class="partner"><span class="square"></span>Ridgefall Clash</span>
      <span class="partner"><span class="dot"></span>Stride Loop</span>
      <span class="partner"><span class="dot"></span>Velmora</span>
      <span class="partner"><span class="square"></span>Corvane Peak</span>
      <span class="partner"><span class="dot"></span>Tessor Karting</span>
    </section>
  </main>
</body>
</html>
```